バイカラータイプのマスクのパッケージデザイン(箱デザイン)を依頼させていただきます。
気軽にカラーマスクを選び、日常的に使っていただけるよう、シンプルで身近なデザインを希望します。
中身(実際のカラー)が確認できるよう、小窓のある箱にしようと考えております。
カラーの他にも不織布の素材や、マスク内側も色付きになっていること、顔にフィットするきれいな形であることをアピールできればと思っております。
バイカラーマスクも数多くありますが、その中でも目に留まるようなデザインをお願いしたいです。
箱サイズ:W18.0cm×H16.5cm×D12.0cm
特に決めておりません。お任せしたいです。
• イラストレーター形式 (.ai)
パッケージサンプル、弊社バイカラーマスクサンプル画像、パッケージ裏面に記載していただきたい詳細を書いた資料を添付しております。
表面、側面、裏面データを展開図にて作成お願いいたします。
カラーが3種ですので、3パターンお願いいたします。

やわらかい色合いと、やさしい雰囲気のあるデザインが、スパンレースというやさしい生地の良さを表していると思いました。
またデザインの全体的にやさしい感じが、親しみやすく手に取ってもらいやすいかなと思いましたので選ばせていただきました。

この度は作品をご提案いただき、誠にありがとうございました。
どのデザインも素晴らしい作品ばかりでした。
今後も利用させていただき、素敵なデザインに出会えればと思っておりますので、
その際はまたご応募いただけますと幸いです。
ありがとうございました。

```html
<!DOCTYPE html>
<html lang="ja">
<head>
<meta charset="utf-8">
<title>3D立体型スパンレース不織布カラーマスク パッケージ 3色</title>
<link href="https://fonts.googleapis.com/css2?family=Zen+Maru+Gothic:wght@400;500;700&family=Shippori+Mincho:wght@500;700&family=Yomogi&family=Great+Vibes&display=swap" rel="stylesheet">
<style>
  :root{
    --paper:#fbf8f5;
    --stripe:#f1ebe6;
    --ink:#4a3f3b;
    --soft-ink:#6f6360;
    --gold:#c8a064;
    --orange:#e79a3c;
    --wine:#76223b;
    --rose:#c65a78;
    --terra:#b86b44;
  }
  *{box-sizing:border-box;margin:0;padding:0}
  html,body{width:1200px;height:2892px;overflow:hidden;background:#ffffff}
  body{font-family:"Zen Maru Gothic",sans-serif;color:var(--ink);position:relative}

  .package{
    position:absolute;left:0;width:1200px;height:912px;overflow:hidden;
    background:repeating-linear-gradient(120deg,var(--paper) 0 26px,var(--stripe) 26px 28px);
  }
  .package--wine{top:32px;--accent:var(--wine);--tint-a:#efdcd8;--tint-b:#ece2da;--swatch:#e8d6cc;--swatch-2:#ead9d2}
  .package--rose{top:976px;--accent:var(--rose);--tint-a:#e6dfee;--tint-b:#e7e1ed;--swatch:#eef0f7;--swatch-2:#b9c3d6}
  .package--terra{top:1920px;--accent:var(--terra);--tint-a:#efe2d6;--tint-b:#ede4db;--swatch:#e9e5d6;--swatch-2:#c7a68a}

  .catch{
    position:absolute;left:168px;top:44px;width:330px;
    font-family:"Yomogi",cursive;font-size:19px;line-height:1.45;color:var(--soft-ink);
    transform:rotate(-4deg);
  }
  .portrait{
    position:absolute;left:330px;top:30px;width:480px;height:560px;
    border-radius:46% 46% 30% 30%;
    background:radial-gradient(ellipse at 50% 58%,#ffffff 0 40%,rgba(255,255,255,0) 72%),
               linear-gradient(180deg,rgba(120,100,95,.10),rgba(120,100,95,.03));
  }
  .feature{
    position:absolute;border-radius:50%;
    display:flex;align-items:center;justify-content:center;text-align:center;
    font-size:21px;line-height:1.45;color:var(--ink);font-weight:500;
  }
  .feature--fabric{left:140px;top:180px;width:230px;height:230px;background:var(--tint-a)}
  .feature--shape{left:140px;top:380px;width:230px;height:180px}
  .feature--ear{left:722px;top:50px;width:186px;height:186px;background:var(--tint-b);font-size:20px}

  .color-label{
    position:absolute;left:1030px;top:86px;
    font-family:"Great Vibes",cursive;font-size:40px;color:#9a8c86;transform:rotate(-8deg);
  }
  .swatch{position:absolute;border-radius:50%;border:3px solid #ffffff;box-shadow:0 2px 8px rgba(0,0,0,.06)}
  .swatch--front{left:910px;top:145px;width:250px;height:250px;background:radial-gradient(circle at 45% 45%,var(--swatch) 0 55%,#f4efe9 56% 100%)}
  .swatch--inner{left:910px;top:380px;width:240px;height:200px;border-radius:46%;background:radial-gradient(circle at 50% 50%,var(--swatch-2) 0 50%,#f1ece6 51% 100%)}
  .inner-badge{
    position:absolute;left:1040px;top:530px;width:96px;height:96px;border-radius:50%;
    background:var(--orange);color:#fff;font-size:18px;font-weight:700;line-height:1.25;
    display:flex;align-items:center;justify-content:center;text-align:center;
  }

  .title{
    position:absolute;left:0;width:1000px;top:622px;text-align:center;
    font-family:"Shippori Mincho",serif;font-weight:700;font-size:42px;letter-spacing:1px;color:var(--accent);
    white-space:nowrap;
  }
  .variant{
    position:absolute;left:0;width:1000px;top:690px;text-align:center;font-size:24px;color:var(--ink);letter-spacing:2px;
  }
  .variant ruby rt{font-size:11px;color:var(--soft-ink);letter-spacing:1px}
  .count{
    position:absolute;left:1010px;top:660px;width:134px;height:58px;border:2px solid var(--accent);
    color:var(--accent);font-size:30px;font-weight:700;display:flex;align-items:center;justify-content:center;background:#fff;
  }
  .spec{
    position:absolute;left:0;right:0;top:796px;display:flex;justify-content:center;align-items:center;gap:12px;
    font-size:22px;color:var(--ink);
  }
  .spec__tag{background:var(--gold);color:#fff;padding:4px 12px;font-weight:700}
  .band{position:absolute;left:0;right:0;bottom:0;height:26px;background:var(--accent)}
  .rule{position:absolute;left:0;right:0;bottom:48px;height:2px;background:var(--accent);opacity:.35}
</style>
</head>
<body>

<section class="package package--wine" aria-label="ピンクベージュ×ワインレッド">
  <p class="catch">毎日のコーデをもっと楽しく♪<br>気分で選べるカラーマスク</p>
  <div class="portrait" role="img" aria-label="マスクを着けた女性の線画イラスト"></div>
  <div class="feature feature--fabric">さらふわ触感の<br>スパンレース<br>不織布</div>
  <div class="feature feature--shape">立体構造で<br>フェイスラインを<br>美しく</div>
  <div class="feature feature--ear">痛くなりにくい<br>幅広耳ゴム</div>
  <span class="color-label">Color</span>
  <div class="swatch swatch--front" role="img" aria-label="マスク正面のカラー写真"></div>
  <div class="swatch swatch--inner" role="img" aria-label="マスク内側のカラー写真"></div>
  <div class="inner-badge">内側も<br>色付き！</div>
  <h2 class="title">3D立体型スパンレース不織布カラーマスク</h2>
  <p class="variant">〈 <ruby>ピンクベージュ<rt>マスクカラー</rt></ruby> × <ruby>ワインレッド<rt>耳ひもカラー</rt></ruby> 〉</p>
  <div class="count">50枚入</div>
  <div class="spec">高機能三層構造フィルター <span class="spec__tag">ウイルス飛沫</span><span class="spec__tag">花粉</span><span class="spec__tag">黄砂</span> 等のミクロ粒子をしっかりブロック</div>
  <div class="rule"></div>
  <div class="band"></div>
</section>

<section class="package package--rose" aria-label="ソフトライラック×ローズピンク">
  <p class="catch">毎日のコーデをもっと楽しく♪<br>気分で選べるカラーマスク</p>
  <div class="portrait" role="img" aria-label="マスクを着けた女性の線画イラスト"></div>
  <div class="feature feature--fabric">さらふわ触感の<br>スパンレース<br>不織布</div>
  <div class="feature feature--shape">立体構造で<br>フェイスラインを<br>美しく</div>
  <div class="feature feature--ear">痛くなりにくい<br>幅広耳ゴム</div>
  <span class="color-label">Color</span>
  <div class="swatch swatch--front" role="img" aria-label="マスク正面のカラー写真"></div>
  <div class="swatch swatch--inner" role="img" aria-label="マスク内側のカラー写真"></div>
  <div class="inner-badge">内側も<br>色付き！</div>
  <h2 class="title">3D立体型スパンレース不織布カラーマスク</h2>
  <p class="variant">〈 <ruby>ソフトライラック<rt>マスクカラー</rt></ruby> × <ruby>ローズピンク<rt>耳ひもカラー</rt></ruby> 〉</p>
  <div class="count">50枚入</div>
  <div class="spec">高機能三層構造フィルター <span class="spec__tag">ウイルス飛沫</span><span class="spec__tag">花粉</span><span class="spec__tag">黄砂</span> 等のミクロ粒子をしっかりブロック</div>
  <div class="rule"></div>
  <div class="band"></div>
</section>

<section class="package package--terra" aria-label="ナチュラルベージュ×ピンク">
  <p class="catch">毎日のコーデをもっと楽しく♪<br>気分で選べるカラーマスク</p>
  <div class="portrait" role="img" aria-label="マスクを着けた女性の線画イラスト"></div>
  <div class="feature feature--fabric">さらふわ触感の<br>スパンレース<br>不織布</div>
  <div class="feature feature--shape">立体構造で<br>フェイスラインを<br>美しく</div>
  <div class="feature feature--ear">痛くなりにくい<br>幅広耳ゴム</div>
  <span class="color-label">Color</span>
  <div class="swatch swatch--front" role="img" aria-label="マスク正面のカラー写真"></div>
  <div class="swatch swatch--inner" role="img" aria-label="マスク内側のカラー写真"></div>
  <div class="inner-badge">内側も<br>色付き！</div>
  <h2 class="title">3D立体型スパンレース不織布カラーマスク</h2>
  <p class="variant">〈 <ruby>ナチュラルベージュ<rt>マスクカラー</rt></ruby> × <ruby>ピンク<rt>耳ひもカラー</rt></ruby> 〉</p>
  <div class="count">50枚入</div>
  <div class="spec">高機能三層構造フィルター <span class="spec__tag">ウイルス飛沫</span><span class="spec__tag">花粉</span><span class="spec__tag">黄砂</span> 等のミクロ粒子をしっかりブロック</div>
  <div class="rule"></div>
  <div class="band"></div>
</section>

</body>
</html>
```